Sex Trafficked women Empowered Business Card Design Project

I would like a two-sided business card. On the front, please include: Marta Oberlin, Executive Director 555-284-7316, www.tallowcrest.org, marta@tallowcrest.org and logo.

On the back:
Vision
Survivors of sexual exploitation live free, fulfilling their God-given purpose.

Perhaps a QR code to direct them to the website: www.tallowcrest.org

I want to try a deeper color for the logo. i have added these files.

My desire is to communicate hope, freedom and new life.
Updates

i decided to ask for business card designs with a deeper toned logo. see new files attached

i have placed the vertical logo as an option, but i would still want the logo with tagline used.

Target Market(s)

I want a professional look to appeal to donors who have a heart to help sexually exploited women. I chose a logo that was light enough to look good on a variety of backgrounds. I do want the logo to catch attention.

Industry/Entity Type

Business

Font styles to use
Serif

Requirements
Must have
• i want to be able to read the tagline. Also, the design should match the look and feel of the logo.

Nice to have
• Since there isn't much text on the back, feel free to be a bit more creative. I still want a professional look.

```html
<!DOCTYPE html>
<html lang="en">
<head>
<meta charset="utf-8">
<title>Tallowcrest Business Card</title>
<link rel="stylesheet" href="https://fonts.googleapis.com/css2?family=Cormorant+Garamond:ital,wght@0,700;1,600;1,700&family=Lato:wght@400;700;900&display=swap">
<style>
  :root {
    --page: #e7e8eb;
    --card: #fbfbfb;
    --ink: #141414;
    --ink-soft: #3a3a3a;
    --blue: #1a7fd8;
    --blue-deep: #0f6cc4;
    --gold: #e2b516;
  }
  * { box-sizing: border-box; margin: 0; padding: 0; }
  html, body {
    width: 1200px;
    height: 985px;
    overflow: hidden;
    background: var(--page);
  }
  .sheet {
    width: 1200px;
    height: 985px;
    display: flex;
    flex-direction: column;
    align-items: center;
    justify-content: center;
    gap: 48px;
  }
  .card {
    position: relative;
    width: 760px;
    height: 434px;
    background: var(--card);
    box-shadow: 0 6px 22px rgba(0,0,0,.18);
    overflow: hidden;
  }
  .card-bands {
    position: absolute;
    inset: 0;
    width: 100%;
    height: 100%;
  }
  .band-blue { fill: var(--blue); }
  .band-gold { fill: var(--gold); }

  .brand {
    position: absolute;
    display: flex;
    align-items: center;
    gap: 22px;
  }
  .brand-dot {
    width: 112px;
    height: 112px;
    border-radius: 50%;
    background: var(--blue);
    flex: none;
  }
  .brand-text { display: flex; flex-direction: column; }
  .brand-name {
    font-family: "Cormorant Garamond", serif;
    font-weight: 700;
    font-size: 52px;
    color: var(--ink);
    line-height: 1;
  }
  .brand-tagline {
    font-family: "Cormorant Garamond", serif;
    font-style: italic;
    font-weight: 600;
    font-size: 22px;
    color: var(--ink-soft);
    align-self: flex-end;
    margin-top: 4px;
  }

  /* back */
  .card-back .brand { left: 110px; top: 74px; }
  .vision {
    position: absolute;
    left: 150px;
    right: 70px;
    top: 240px;
    font-family: "Cormorant Garamond", serif;
    font-style: italic;
    font-weight: 700;
    font-size: 31px;
    line-height: 1.3;
    color: var(--ink-soft);
    text-align: center;
  }

  /* front */
  .card-front .brand { left: 70px; top: 56px; }
  .holder {
    position: absolute;
    right: 62px;
    top: 200px;
    text-align right;
    text-align: right;
    font-family: "Lato", sans-serif;
  }
  .holder-name {
    font-weight: 900;
    font-size: 24px;
    color: var(--blue-deep);
    letter-spacing: .5px;
    text-transform: uppercase;
  }
  .holder-title {
    font-weight: 700;
    font-size: 17px;
    color: var(--ink);
  }
  .contacts {
    position: absolute;
    left: 70px;
    top: 262px;
    list-style: none;
    font-family: "Lato", sans-serif;
    font-weight: 700;
    font-size: 21px;
    color: var(--ink-soft);
  }
  .contacts li {
    display: flex;
    align-items: center;
    gap: 16px;
    height: 38px;
  }
  .contact-icon {
    width: 22px;
    height: 22px;
    fill: none;
    stroke: var(--blue);
    stroke-width: 2.2;
    stroke-linecap: round;
    stroke-linejoin: round;
    flex: none;
  }
  .contact-icon.solid { fill: var(--blue); stroke: none; }
</style>
</head>
<body>
<main class="sheet">

  <section class="card card-back" aria-label="Business card back">
    <svg class="card-bands" viewBox="0 0 760 434" preserveAspectRatio="none" aria-hidden="true">
      <path class="band-blue" d="M0,422 L600,416 L600,434 L0,434 Z"/>
      <path class="band-gold" d="M548,434 C566,414 586,408 620,408 L760,406 L760,434 Z"/>
    </svg>
    <div class="brand">
      <span class="brand-dot"></span>
      <div class="brand-text">
        <span class="brand-name">Tallowcrest</span>
        <span class="brand-tagline">Where new life takes root</span>
      </div>
    </div>
    <p class="vision">Survivors of sexual exploitation live free,<br>fulfilling their God-given purpose.</p>
  </section>

  <section class="card card-front" aria-label="Business card front">
    <svg class="card-bands" viewBox="0 0 760 434" preserveAspectRatio="none" aria-hidden="true">
      <path class="band-blue" d="M0,422 L600,416 L600,434 L0,434 Z"/>
      <path class="band-gold" d="M548,434 C566,414 586,408 620,408 L760,406 L760,434 Z"/>
    </svg>
    <div class="brand">
      <span class="brand-dot"></span>
      <div class="brand-text">
        <span class="brand-name">Tallowcrest</span>
        <span class="brand-tagline">Where new life takes root</span>
      </div>
    </div>
    <div class="holder">
      <p class="holder-name">Marta Oberlin</p>
      <p class="holder-title">Executive Director</p>
    </div>
    <ul class="contacts">
      <li>
        <svg class="contact-icon solid" viewBox="0 0 24 24" aria-hidden="true">
          <path d="M3 9c0-3 4-5 9-5s9 2 9 5v2h-5V9c-1-.6-2.4-1-4-1s-3 .4-4 1v2H3z"/>
          <rect x="5" y="13" width="14" height="8" rx="1.5"/>
        </svg>
        <span>555-284-7316</span>
      </li>
      <li>
        <svg class="contact-icon solid" viewBox="0 0 24 24" aria-hidden="true">
          <path d="M2 5h20v14H2z"/>
          <path d="M2 5l10 8 10-8" fill="none" stroke="#fbfbfb" stroke-width="1.8"/>
        </svg>
        <span>www.tallowcrest.org</span>
      </li>
      <li>
        <svg class="contact-icon" viewBox="0 0 24 24" aria-hidden="true">
          <path d="M10 14a4 4 0 0 0 5.7 0l3.6-3.6a4 4 0 0 0-5.7-5.7L12 6.3"/>
          <path d="M14 10a4 4 0 0 0-5.7 0l-3.6 3.6a4 4 0 0 0 5.7 5.7L12 17.7"/>
        </svg>
        <span>marta@tallowcrest.org</span>
      </li>
    </ul>
  </section>

</main>
</body>
</html>
```